New Business Card Design Project

I need a clean, professional business card. I'd like it to have some color, but not be wild. We do technology consulting and we have clients large and small who trust us with some of their most important data and projects. Simple but not boring should drive all design proposals. Multicolored and two sided, but with a matte finish, I think.
For more on tone, check out our website: http://brindlequay.com

Target Market(s)

Upper management of respected businesses. Tech savvy, but not "hipster".

Industry/Entity Type

Business

Requirements
Must have
• Files need to be provided in .eps and in .pdf in a manner that allows for easy updates.
Must have Name, Title, Phone, Email, Twitter, Website
Nice to have
• Logo/Name shouldn't be too big. One thing I've read several places is that the bigger the logo, the smaller the brand. A good article on dos and don'ts here: http://www.mossvane.com/2011/02/business-card-experience.html

```html
<!DOCTYPE html>
<html lang="en">
<head>
<meta charset="utf-8">
<title>Brindle Quay – Business Card</title>
<link rel="stylesheet" href="https://fonts.googleapis.com/css2?family=Montserrat:wght@300;400&family=Ubuntu:wght@300;400&display=swap">
<style>
  :root {
    --backdrop: #2b2522;
    --card: #161616;
    --card-edge: #202020;
    --teal: #3fb5c8;
    --green: #9bcc3c;
    --silver: #b8bbbe;
    --muted: #8d9093;
  }
  * { margin: 0; padding: 0; box-sizing: border-box; }
  html, body {
    width: 1200px;
    height: 716px;
    overflow: hidden;
    background: var(--backdrop);
  }
  .canvas {
    position: relative;
    width: 1200px;
    height: 716px;
    display: flex;
    align-items: center;
    justify-content: center;
    gap: 60px;
  }
  .card {
    position: relative;
    width: 500px;
    height: 286px;
    background: var(--card);
    border: 1px solid var(--card-edge);
    box-shadow: 0 18px 40px rgba(0, 0, 0, 0.55);
  }
  .brand {
    display: flex;
    align-items: center;
    gap: 12px;
  }
  .brand-mark {
    width: 14px;
    height: 14px;
    background: var(--teal);
  }
  .brand-name {
    font-family: "Montserrat", sans-serif;
    font-weight: 300;
    letter-spacing: 0.06em;
    color: var(--silver);
    text-transform: uppercase;
  }

  /* front */
  .card-front .brand {
    position: absolute;
    left: 48px;
    top: 118px;
  }
  .card-front .brand-name { font-size: 27px; }
  .website {
    position: absolute;
    left: 48px;
    top: 160px;
    font-family: "Ubuntu", sans-serif;
    font-weight: 300;
    font-size: 12px;
    letter-spacing: 0.32em;
    color: var(--silver);
  }
  .website .domain { color: var(--teal); }

  /* back */
  .card-back .brand {
    position: absolute;
    left: 44px;
    top: 52px;
  }
  .card-back .brand-name { font-size: 29px; }
  .contact-list {
    position: absolute;
    left: 44px;
    bottom: 52px;
    list-style: none;
    font-family: "Ubuntu", sans-serif;
    font-weight: 300;
    font-size: 12px;
    line-height: 1.75;
    color: var(--muted);
  }
  .contact-label { display: inline-block; width: 50px; }
  .label-phone { color: var(--teal); }
  .label-email { color: var(--green); }
  .label-twitter { color: var(--teal); }
  .person {
    position: absolute;
    right: 48px;
    bottom: 50px;
    font-family: "Ubuntu", sans-serif;
  }
  .person-name {
    font-size: 16px;
    font-weight: 400;
  }
  .person-first { color: var(--teal); }
  .person-last { color: var(--green); }
  .person-title {
    font-size: 11px;
    font-weight: 300;
    color: var(--muted);
    letter-spacing: 0.05em;
  }
</style>
</head>
<body>
<main class="canvas">
  <section class="card card-front" aria-label="Card front">
    <div class="brand">
      <span class="brand-mark"></span>
      <span class="brand-name">Brindle Quay</span>
    </div>
    <p class="website">www.<span class="domain">brindlequay</span>.com</p>
  </section>

  <section class="card card-back" aria-label="Card back">
    <div class="brand">
      <span class="brand-mark"></span>
      <span class="brand-name">Brindle Quay</span>
    </div>
    <ul class="contact-list">
      <li><span class="contact-label label-phone">Phone</span>: 555.013.4821</li>
      <li><span class="contact-label label-email">Email</span>: dana@brindlequay.com</li>
      <li><span class="contact-label label-twitter">Twitter</span>: @BrindleQuay</li>
    </ul>
    <div class="person">
      <p class="person-name"><span class="person-first">Dana</span> <span class="person-last">Morrell</span></p>
      <p class="person-title">CEO</p>
    </div>
  </section>
</main>
</body>
</html>
```